Stationary & Business cards for Onsite Wastewater Company
Brindlecove Septic Systems Ltd.
Stationary & Business cards for Onsite Wastewater Company - Construction
Creative Brief
Professional
Dwight Amberole
6172 Pellworth St. Langley, B.C. V3K8R2
dwight@brindlecoveseptic-example.com
brindlecoveseptic-example.com
I would like it to say: Design & Build on the front of the card
Open to ideas: maybe use the logo with black background
lanternmoth lanternmoth

```html
<!DOCTYPE html>
<html lang="en">
<head>
<meta charset="utf-8">
<title>Brindlecove Septic Systems Ltd. – Business Card</title>
<link href="https://fonts.googleapis.com/css2?family=Oswald:wght@600&family=Open+Sans:wght@400;700&display=swap" rel="stylesheet">
<style>
  :root {
    --bg: #d9dadb;
    --card: #ffffff;
    --ink: #1d1d1f;
    --band: #141416;
    --blue: #1f73c9;
    --blue-light: #5aa6ea;
    --text: #3a3a3c;
  }
  * { box-sizing: border-box; margin: 0; padding: 0; }
  html, body { width: 1200px; height: 984px; overflow: hidden; }
  body {
    background: var(--bg);
    font-family: "Open Sans", sans-serif;
    position: relative;
  }
  .card {
    position: absolute;
    left: 250px;
    width: 700px;
    height: 400px;
    background: var(--card);
    border-radius: 26px;
    overflow: hidden;
    box-shadow: 0 10px 28px rgba(0,0,0,.18);
  }
  .card--front { top: 62px; }
  .card--back { top: 522px; }

  .brand-name {
    font-family: "Oswald", sans-serif;
    font-weight: 600;
    color: var(--ink);
    text-transform: uppercase;
    line-height: 1.05;
    letter-spacing: 1px;
  }
  .card--front .brand {
    position: absolute;
    left: 50%; top: 50%;
    transform: translate(-50%, -50%);
    text-align: center;
  }
  .card--front .brand-name { font-size: 46px; }
  .card--front .brand-name small { display: block; font-size: 25px; letter-spacing: 3px; }

  .swoosh { position: absolute; inset: 0; width: 100%; height: 100%; }

  .contact {
    position: absolute;
    left: 52px; top: 92px;
    font-size: 15px;
    line-height: 1.5;
    color: var(--text);
  }
  .contact .person { font-weight: 700; font-size: 17px; color: var(--ink); margin-bottom: 8px; }
  .contact .address { margin-bottom: 14px; }

  .card--back .brand {
    position: absolute;
    right: 42px; bottom: 36px;
    text-align: right;
  }
  .tagline { font-size: 14px; color: var(--text); margin-bottom: 4px; }
  .card--back .brand-name { font-size: 36px; }
  .card--back .brand-name small { display: block; font-size: 20px; letter-spacing: 2px; }
</style>
</head>
<body>
  <section class="card card--front" aria-label="Card front">
    <div class="brand">
      <p class="brand-name">Brindlecove<small>Septic Systems Ltd.</small></p>
    </div>
  </section>

  <section class="card card--back" aria-label="Card back">
    <svg class="swoosh" viewBox="0 0 700 400" preserveAspectRatio="none" aria-hidden="true">
      <path d="M0 0 H700 V250 C600 245 540 175 440 95 C360 35 230 20 0 40 Z" fill="var(--band)"/>
      <path d="M0 40 C230 20 360 35 440 95 C540 175 600 245 700 250 V268 C590 265 530 195 432 115 C355 55 225 40 0 55 Z" fill="var(--blue)"/>
      <path d="M0 58 C225 43 352 60 428 120 C525 200 585 272 700 274" fill="none" stroke="var(--blue-light)" stroke-width="3"/>
      <path d="M0 70 C220 56 345 74 420 132 C515 210 578 285 700 286" fill="none" stroke="var(--blue)" stroke-width="1.5"/>
    </svg>
    <div class="contact">
      <p class="person">Dwight Amberole</p>
      <p class="address">6172 Pellworth St.<br>Langley, B.C.<br>V3K8R2</p>
      <p>Cell: 604-555-0142<br>Fax: 604-555-0187<br>Email: dwight@brindlecoveseptic-example.com<br>brindlecoveseptic-example.com</p>
    </div>
    <div class="brand">
      <p class="tagline">Design &amp; Build</p>
      <p class="brand-name">Brindlecove<small>Septic Systems Ltd.</small></p>
    </div>
  </section>
</body>
</html>
```